Velmora Biz Card 2019

New business card for Velmora Property Inspections. We are a residential home inspection company in Arizona.

Target Market(s)

Real Estate

Font styles to use
Sans Serif

Requirements
Must have
• Glen Mirewick
• Home Inspector
• Velmora Property Inspections, LLC
• 480-555-0172
• glen@velmora-llc.example

```html
<!DOCTYPE html>
<html lang="en">
<head>
<meta charset="utf-8">
<title>Velmora Biz Card 2019</title>
<link href="https://fonts.googleapis.com/css2?family=Open+Sans:wght@400;600;700;800&display=swap" rel="stylesheet">
<style>
  :root {
    --bg: #e8e6e4;
    --card: #ffffff;
    --green: #4cb648;
    --grey: #5b5c5e;
    --text: #55575a;
    --navy: #27324a;
    --photo-light: #eef0f1;
  }
  * { box-sizing: border-box; margin: 0; padding: 0; }
  html, body { width: 1200px; height: 997px; overflow: hidden; }
  body {
    background: var(--bg);
    font-family: "Open Sans", Arial, sans-serif;
    position: relative;
  }
  .card {
    position: absolute;
    width: 540px;
    height: 309px;
    background: var(--card);
    box-shadow: 0 6px 18px rgba(0,0,0,0.12);
    overflow: hidden;
  }
  .card-front { left: 40px; top: 200px; }
  .card-back  { left: 620px; top: 470px; }

  .brand-name {
    font-weight: 800;
    color: var(--grey);
    letter-spacing: 1px;
    display: flex;
    align-items: center;
    gap: 10px;
  }
  .brand-mark { width: 14px; height: 14px; background: var(--green); display: inline-block; }

  .front-brand { position: absolute; right: 26px; top: 20px; font-size: 30px; }

  .contact-list {
    position: absolute; right: 26px; top: 74px;
    list-style: none; text-align: right;
    font-size: 12.5px; color: var(--text); line-height: 19px;
  }
  .contact-list li { display: flex; justify-content: flex-end; align-items: center; gap: 7px; }
  .contact-list svg { width: 11px; height: 11px; }

  .rule { position: absolute; left: 215px; right: 0; top: 146px; height: 4px; background: var(--green); }

  .company {
    position: absolute; right: 26px; top: 160px; text-align: right;
    color: var(--text); font-size: 12.5px; line-height: 18px;
  }
  .company-name { font-weight: 700; }

  .name-band {
    position: absolute; left: 228px; right: 0; top: 212px; height: 26px;
    background: var(--green); color: #fff;
    display: flex; align-items: center; padding-left: 14px; gap: 10px;
  }
  .person-name { font-weight: 700; font-size: 15px; letter-spacing: 0.3px; text-transform: uppercase; }
  .person-title { font-size: 12.5px; }

  .photo {
    position: absolute; left: 0; bottom: 0; width: 228px; height: 200px;
    background: linear-gradient(180deg, var(--photo-light) 0%, #c9cfd5 45%, var(--navy) 75%, var(--navy) 100%);
  }

  .back-brand {
    position: absolute; left: 0; right: 0; top: 50%;
    transform: translateY(-50%);
    justify-content: center; font-size: 44px;
  }
  .back-brand .brand-mark { width: 20px; height: 20px; }
</style>
</head>
<body>

<section class="card card-front">
  <div class="brand-name front-brand"><span class="brand-mark"></span>VELMORA</div>

  <ul class="contact-list">
    <li>480-555-0172
      <svg viewBox="0 0 12 12"><path d="M2.5 1l2 2.2-1 1.3c.8 1.6 2 2.8 3.5 3.5l1.3-1 2.2 2-1.2 1.8C5 10.5 1.5 7 .8 2.2z" fill="#4cb648"/></svg>
    </li>
    <li>glen@velmora-llc.example
      <svg viewBox="0 0 12 12"><rect x="1" y="3" width="10" height="7" fill="#4cb648"/><path d="M1 3l5 4 5-4" stroke="#fff" fill="none"/></svg>
    </li>
    <li>www.velmora-llc.example
      <svg viewBox="0 0 12 12"><circle cx="6" cy="6" r="5" fill="#4cb648"/><path d="M1 6h10M6 1c-2.5 3-2.5 7 0 10M6 1c2.5 3 2.5 7 0 10" stroke="#fff" stroke-width=".8" fill="none"/></svg>
    </li>
  </ul>

  <div class="rule"></div>

  <div class="company">
    <p class="company-name">Velmora Property Inspections, LLC</p>
    <p>P.O. Box-052, Street Name, City Name, 000 000</p>
  </div>

  <div class="photo" role="img" aria-label="Portrait photo of the home inspector in a navy polo shirt"></div>

  <div class="name-band">
    <span class="person-name">Glen Mirewick</span>
    <span class="person-title">Home Inspector</span>
  </div>
</section>

<section class="card card-back">
  <div class="brand-name back-brand"><span class="brand-mark"></span>VELMORA</div>
</section>

</body>
</html>
```